New Business Card Design*

We are a recruitment company based in Norwich/Cambridge England.
I have included our company logo which we want to remain the same.

What we are looking for is a new creative Business card which will really stand out!!

Contact Information for Business Card

Harriet Vance
email: Harriet@brelvix.co.uk
Address: Tolworth House
Ashgrove Innovation Park
Pelham Road
Norwich
KT9 3QD
Tel:01632 960418

```html
<!DOCTYPE html>
<html lang="en">
<head>
<meta charset="utf-8">
<title>Brelvix Business Card</title>
<link rel="stylesheet" href="https://fonts.googleapis.com/css2?family=Roboto:wght@400;500&display=swap">
<style>
  :root {
    --backdrop: #1b1b1c;
    --card: #202021;
    --accent: #7dc242;
    --text-light: #ffffff;
    --text-muted: #8e8b90;
  }
  * { box-sizing: border-box; margin: 0; padding: 0; }
  html, body {
    width: 1200px; height: 900px; overflow: hidden;
    background: var(--backdrop);
    font-family: "Roboto", Arial, sans-serif;
  }
  .stage {
    position: relative; width: 1200px; height: 900px;
  }
  .card {
    position: absolute; left: 250px; width: 700px; height: 400px;
    background: var(--card);
    border-bottom: 6px solid var(--accent);
    box-shadow: 0 12px 30px rgba(0,0,0,0.55);
  }
  .card--front { top: 40px; }
  .card--back { top: 465px; }

  .brand {
    position: absolute; left: 0; right: 0;
    display: flex; flex-direction: column; align-items: center;
  }
  .card--front .brand { top: 130px; }
  .card--back .brand { top: 60px; }
  .brand__row { display: flex; align-items: center; gap: 16px; }
  .brand__dot {
    width: 58px; height: 58px; border-radius: 50%;
    background: var(--accent);
  }
  .brand__name {
    font-weight: 500; font-size: 62px; color: var(--accent);
    letter-spacing: 1px; line-height: 1;
  }
  .card--back .brand__dot { width: 50px; height: 50px; }
  .card--back .brand__name { font-size: 54px; }
  .brand__tagline {
    margin-top: 8px; margin-left: 74px;
    font-size: 12px; letter-spacing: 5px; color: var(--text-muted);
  }

  .holder {
    position: absolute; top: 188px; left: 0; right: 0;
    text-align: center;
    font-weight: 500; font-size: 26px; letter-spacing: 2px;
    color: var(--accent); text-transform: uppercase;
  }

  .details {
    position: absolute; top: 245px; left: 0; right: 0;
    display: flex; justify-content: center;
  }
  .address {
    text-align: right; padding-right: 26px;
    font-size: 19px; line-height: 24px; color: var(--text-light);
  }
  .address__building { color: var(--accent); }
  .divider { width: 2px; height: 92px; background: var(--accent); }
  .contact {
    list-style: none; padding-left: 22px; padding-top: 18px;
    font-size: 19px; line-height: 24px; color: var(--text-light);
  }
  .contact li { display: flex; align-items: center; gap: 10px; }
  .contact svg { width: 16px; height: 16px; flex: none; }
  .contact__domain { color: var(--accent); }
</style>
</head>
<body>
<main class="stage">
  <section class="card card--front">
    <div class="brand">
      <div class="brand__row">
        <span class="brand__dot"></span>
        <span class="brand__name">Brelvix</span>
      </div>
      <span class="brand__tagline">Technology Recruitment</span>
    </div>
  </section>

  <section class="card card--back">
    <div class="brand">
      <div class="brand__row">
        <span class="brand__dot"></span>
        <span class="brand__name">Brelvix</span>
      </div>
      <span class="brand__tagline">Technology Recruitment</span>
    </div>

    <h1 class="holder">Harriet Vance</h1>

    <div class="details">
      <address class="address" style="font-style: normal;">
        <span class="address__building">Tolworth House</span><br>
        Ashgrove Innovation Park<br>
        Pelham Road Norwich KT9 3QD
      </address>
      <span class="divider"></span>
      <ul class="contact">
        <li>
          <svg viewBox="0 0 16 16" aria-hidden="true"><rect width="16" height="16" rx="2" fill="#7dc242"/><path d="M5 3.5l2 2-1.2 1.4c.6 1.4 1.8 2.6 3.3 3.3L10.5 9l2 2-1.3 1.6C7.6 12.3 3.7 8.4 3.4 4.8z" fill="#202021"/></svg>
          01632 960418
        </li>
        <li>
          <svg viewBox="0 0 16 16" aria-hidden="true"><rect x="1" y="3" width="14" height="10" fill="#7dc242"/><path d="M1 3l7 6 7-6" fill="none" stroke="#202021" stroke-width="1.3"/></svg>
          Harriet@brelvix.co.uk
        </li>
        <li>
          <svg viewBox="0 0 16 16" aria-hidden="true"><circle cx="8" cy="8" r="7" fill="#7dc242"/><path d="M1 8h14M8 1c-3 3-3 11 0 14M8 1c3 3 3 11 0 14" fill="none" stroke="#202021" stroke-width="1"/></svg>
          <span>www.<span class="contact__domain">brelvix</span>.co.uk</span>
        </li>
      </ul>
    </div>
  </section>
</main>
</body>
</html>
```